Business Cards for new orthopaedic surgery practice

My husband and I are starting our own orthopaedic surgery practice. We are looking for a business card that is uniform, but one will have my name/title and the other will have his. You can just create one design with my name on it for now. But when I choose your design as the winning design I will ask that you add another copy with his name/title.

We are looking for classy, simple, elite all in one. We like dark blues/a little gold/yellow. Something that goes with our logo. We want our logo incorporated. Here is all the info you need:
Business name: RV Spine & Vitality Center
Location: 38915 North Bramble Ave
Palm Crest, FL 33482
Phone: 954-218-4630
Fax: 954-571-2846
Email: info@myrvspine.example

Names: Lucinda Ferrow, M.D.
Board Certified Hand and Upper Extremity Surgeon

Emeka Dlunga, M.D.
Board Certified Hip & Knee Replacement/General Orthopaedic Surgeon

Can decide what you want to put on the back. Maybe a slogan:
Steady in Care. Devoted to You

I am just going to upload our logo. The only thing is if we select you as the winning design, the location, and phone numbers may change. We will need your help to update that once fully solidified.

Industry/Entity Type

Medical

Contact Information for Business Card

Colors
0054AA
0677BA
7BADD7
CADEEF
E8F1F8
0094D4
00A9DD
6FCCEA
C7EBF8
E9F6FB

Requirements
Must have
• class, appeal,
Should not have
• We want to air on the side of masculine if we are looking at masculine vs. feminine feel. But we still want it classy, sophisticated, and something we will love

```html
<!DOCTYPE html>
<html lang="en">
<head>
<meta charset="utf-8">
<title>RV Spine &amp; Vitality Center – Business Card</title>
<link rel="stylesheet" href="https://fonts.googleapis.com/css2?family=Montserrat:wght@300;400;600;700&display=swap">
<style>
  :root {
    --navy: #0c1b45;
    --navy-light: #17264f;
    --gold: #b8944e;
    --gold-light: #c4a05a;
    --paper: #f1f1f1;
    --white: #ffffff;
    --stage: #e6e6e6;
  }
  * { margin: 0; padding: 0; box-sizing: border-box; }
  html, body { width: 1200px; height: 1200px; overflow: hidden; }
  body {
    background: var(--stage);
    font-family: "Montserrat", Arial, sans-serif;
    position: relative;
  }
  .card {
    position: absolute;
    left: 180px;
    width: 840px;
    height: 480px;
    overflow: hidden;
    box-shadow: 0 10px 30px rgba(0,0,0,0.18);
  }
  /* Front */
  .card-front {
    top: 90px;
    background: linear-gradient(135deg, var(--navy), var(--navy-light));
  }
  .card-front .brand {
    position: absolute;
    left: 0; right: 0;
    top: 185px;
    justify-content: center;
  }
  .brand {
    display: flex;
    align-items: center;
    gap: 18px;
  }
  .brand-dot {
    width: 34px; height: 34px;
    border-radius: 50%;
    background: var(--gold);
    flex: none;
  }
  .brand-name {
    font-weight: 600;
    font-size: 34px;
    letter-spacing: 1px;
    color: var(--gold);
  }
  .slogan {
    position: absolute;
    left: 0; right: 0;
    top: 372px;
    text-align: center;
    font-weight: 400;
    font-size: 24px;
    color: var(--gold);
    letter-spacing: 0.3px;
  }
  /* Back */
  .card-back {
    top: 630px;
    background: var(--paper);
  }
  .card-back svg.shape { position: absolute; inset: 0; }
  .back-brand {
    position: absolute;
    left: 36px;
    top: 215px;
    width: 330px;
    display: flex;
    align-items: center;
    gap: 12px;
  }
  .back-brand .brand-dot { width: 22px; height: 22px; background: var(--navy); }
  .back-brand .brand-name { font-size: 21px; color: var(--navy); letter-spacing: 0.3px; line-height: 1.25; }
  .contact {
    position: absolute;
    left: 470px;
    top: 48px;
    width: 340px;
    color: var(--white);
  }
  .doctor-name {
    font-weight: 700;
    font-size: 27px;
    color: var(--navy);
  }
  .doctor-title {
    font-weight: 400;
    font-size: 16px;
    line-height: 1.3;
    margin-top: 6px;
  }
  .rule {
    position: relative;
    height: 2px;
    background: var(--white);
    margin: 20px 0 22px;
  }
  .rule::before, .rule::after {
    content: "";
    position: absolute;
    top: -3px;
    width: 8px; height: 8px;
    border-radius: 50%;
    background: var(--white);
  }
  .rule::before { left: -2px; }
  .rule::after { right: -2px; }
  .contact-list { list-style: none; }
  .contact-item {
    display: flex;
    align-items: flex-start;
    gap: 12px;
    font-size: 17px;
    line-height: 1.3;
    margin-bottom: 12px;
  }
  .contact-item.strong { font-weight: 700; }
  .contact-icon {
    flex: none;
    width: 22px; height: 22px;
    border-radius: 50%;
    background: var(--white);
    display: flex; align-items: center; justify-content: center;
    margin-top: 1px;
  }
</style>
</head>
<body>

<section class="card card-front">
  <div class="brand">
    <span class="brand-dot"></span>
    <span class="brand-name">RV Spine &amp; Vitality Center</span>
  </div>
  <p class="slogan">Steady in Care. Devoted to You</p>
</section>

<section class="card card-back">
  <svg class="shape" width="840" height="480" viewBox="0 0 840 480">
    <path d="M410 0 H840 V480 H560 C470 420 430 330 425 230 C420 140 440 60 410 0 Z" fill="var(--gold-light)"/>
    <path d="M395 0 C425 60 405 140 410 230 C415 330 455 420 545 480" fill="none" stroke="var(--white)" stroke-width="8"/>
    <path d="M370 0 C398 50 382 120 386 200" fill="none" stroke="var(--gold)" stroke-width="3"/>
    <path d="M400 380 C430 430 470 460 510 480" fill="none" stroke="var(--gold)" stroke-width="3"/>
  </svg>

  <div class="back-brand">
    <span class="brand-dot"></span>
    <span class="brand-name">RV Spine &amp; Vitality Center</span>
  </div>

  <div class="contact">
    <h1 class="doctor-name">Lucinda Ferrow, M.D.</h1>
    <p class="doctor-title">Board Certified Hand and<br>Upper Extremity Surgeon</p>
    <div class="rule"></div>
    <ul class="contact-list">
      <li class="contact-item">
        <span class="contact-icon">
          <svg width="12" height="10" viewBox="0 0 12 10"><rect x="0.5" y="0.5" width="11" height="9" fill="none" stroke="#b8944e"/><path d="M0.5 0.5 L6 5.5 L11.5 0.5" fill="none" stroke="#b8944e"/></svg>
        </span>
        info@myrvspine.example
      </li>
      <li class="contact-item strong">
        <span class="contact-icon">
          <svg width="12" height="12" viewBox="0 0 12 12"><path d="M2 1 L4.5 1 L5.5 4 L4 5 C4.8 6.8 5.6 7.6 7 8 L8 6.5 L11 7.5 L11 10 C6 11 1 6 2 1 Z" fill="#b8944e"/></svg>
        </span>
        954-218-4630
      </li>
      <li class="contact-item strong">
        <span class="contact-icon">
          <svg width="12" height="12" viewBox="0 0 12 12"><rect x="3" y="1" width="6" height="3" fill="#b8944e"/><rect x="1" y="4.5" width="10" height="4.5" fill="#b8944e"/><rect x="3" y="8" width="6" height="3" fill="none" stroke="#b8944e"/></svg>
        </span>
        954-571-2846
      </li>
      <li class="contact-item">
        <span class="contact-icon">
          <svg width="10" height="13" viewBox="0 0 10 13"><path d="M5 12 C2 8 1 6 1 4.5 A4 4 0 0 1 9 4.5 C9 6 8 8 5 12 Z" fill="#b8944e"/><circle cx="5" cy="4.5" r="1.5" fill="#fff"/></svg>
        </span>
        <span>38915 North Bramble Ave<br>Palm Crest, FL 33482</span>
      </li>
    </ul>
  </div>
</section>

</body>
</html>
```